Logo, letterhead and business card design for fun, different NYC consulting firm

THE BRISTAVEN GROUP - We are looking for an identity package (logo, letterhead, business cards) that makes high-potential entrepreneurs and enterprising corporate executives trip over each other in their race to work with our startup "gurus." We coach and advise individuals (entrepreneurs and corporate executives) and consult organizations (startups and established companies) who want to unlock their entrepreneurial spirit so they can launch new ventures faster, with less investment and greater promise. On the big end, we helped Pelvanix rollout a new line of mobile accessories; on the small side, we helped a Florida woman start an elder care business that now employes 60 people.
Our President is a high-energy, generous guy. He's one of the most fun, approachable, and inspired millionaires I've ever met. His charisma alone makes entrepreneurs and executives of all stripes want to work with him-and these qualities are what we'd like to translate into our logo and other identity pieces.
Please, please, please don't go to the company's website to get a feel for us-the site is horrible, it's not our "vibe," and it's going to be re-imagined, stat!
Instead, know this:
we love startups
we are the home of creative ideas
we support entrepreneurs and enterprising corporate executives in everything they do
we create wealth and value
we help the world
The Bristaven Group is composed of entrepreneur-gurus who are:
fun
independent
born to challenge
unconventional
practical
action-oriented
creative
balanced
Our tagline is:
unlocking the entrepreneurial spirit | nurturing new ventures
Our business includes:
coaching | consulting | advisory
We plan on extending the winning identity to our website, so there may be more work in it for you beyond this initial package (more money, yeah!).
Our letterhead will be used almost exclusively as a background in Microsoft Word (we're not sure if we'll get it printed); and the business card should be double-sided, with an optional 2D barcode (if it works well into your design).
Updates
Dear designers -
Target Market(s)
People and organizations who are looking to launch new business ventures more quickly, affordably, and successfully than the competition
Industry/Entity Type
Investment
Requirements
Must have
- Business cards:
- company name: The Bristaven Group
- web address: www.bristavengroup.example
- physical address: 14 Corvath Road, Westport, CT 06881
- name and title: Paul Denholtz, President
- phone number: 203.555.0148
- e-mail address: pdenholtz@bristavengroup.example
- tagline: unlocking the entrepreneurial spirit | nurturing new ventures
- the card should be double-sided; on the back it should say: coaching | consulting | advisory (it's up to you if you want to put the company name and logo on the back and/or a QR code)
Letterhead:
- company name: The Bristaven Group (along with coaching | consulting | advisory somewhere on the page)

```html
<!DOCTYPE html>
<html lang="en">
<head>
<meta charset="utf-8">
<title>The Bristaven Group – Stationery</title>
<link rel="stylesheet" href="https://fonts.googleapis.com/css2?family=Mulish:wght@400;500;600&display=swap">
<style>
  :root {
    --orange: #f15a29;
    --ink: #3a3a45;
    --paper: #ffffff;
    --edge: #c9c9c9;
    --shadow: rgba(0,0,0,0.28);
  }
  html, body {
    margin: 0;
    padding: 0;
    overflow: hidden;
    background: var(--paper);
  }
  p, ul, address { margin: 0; padding: 0; }
  .canvas {
    position: relative;
    width: 1200px;
    height: 1200px;
    overflow: hidden;
    background: var(--paper);
    font-family: "Mulish", "Avenir Next", sans-serif;
    color: var(--ink);
  }

  /* Brand lockup: invented name + one plain square */
  .brand {
    position: absolute;
    display: flex;
    align-items: flex-end;
    gap: 8px;
  }
  .brand-name {
    font-family: "Mulish", sans-serif;
    font-weight: 600;
    color: var(--ink);
    line-height: 1.05;
    text-align: right;
    white-space: nowrap;
  }
  .brand-mark {
    flex: none;
    border-radius: 6px;
    background: var(--orange);
    align-self: flex-start;
  }
  .brand--mono .brand-mark { background: var(--ink); }

  .brand--hero { left: 96px; top: 168px; }
  .brand--hero .brand-name { font-size: 34px; margin-top: 32px; }
  .brand--hero .brand-mark { width: 60px; height: 54px; }

  .brand--mono-show { left: 126px; top: 350px; }
  .brand--mono-show .brand-name { font-size: 27px; margin-top: 28px; }
  .brand--mono-show .brand-mark { width: 46px; height: 44px; }

  /* Sheets */
  .sheet {
    position: absolute;
    background: var(--paper);
    border: 1px solid var(--edge);
    box-shadow: 4px 4px 6px var(--shadow);
    overflow: hidden;
  }
  .band {
    position: absolute;
    left: 0; right: 0; bottom: 0;
    background: var(--orange);
    color: var(--paper);
    display: flex;
    align-items: center;
    justify-content: center;
    white-space: nowrap;
  }
  .services {
    position: absolute;
    white-space: nowrap;
    letter-spacing: 0.02em;
    line-height: 1.2;
    color: var(--ink);
  }
  .services .sep { color: var(--orange); }

  /* Card front */
  .card-front { left: 68px; top: 680px; width: 288px; height: 188px; }
  .card-front .brand { left: 38px; top: 22px; }
  .card-front .brand-name { font-size: 29px; margin-top: 24px; }
  .card-front .brand-mark { width: 48px; height: 46px; }
  .card-front .services { left: 30px; top: 140px; font-size: 12px; }
  .card-front .band { height: 18px; }

  /* Card back */
  .card-back { left: 68px; top: 904px; width: 288px; height: 188px; }
  .card-back .person { position: absolute; left: 24px; top: 48px; }
  .card-back .person-name { color: var(--orange); font-size: 12px; letter-spacing: 0.02em; }
  .card-back .person-title { font-size: 10.5px; margin-top: 1px; }
  .card-back .contact {
    position: absolute; left: 24px; top: 90px;
    list-style: none;
    font-size: 9.5px; line-height: 13.5px;
  }
  .card-back .contact .key { color: var(--orange); }
  .card-back .contact .web { color: var(--orange); }
  .card-back .band { height: 24px; font-size: 9.5px; }

  /* Letterhead */
  .letterhead { left: 422px; top: 90px; width: 713px; height: 1009px; }
  .letterhead .brand { right: 14px; top: 14px; }
  .letterhead .brand-name { font-size: 29px; margin-top: 24px; }
  .letterhead .brand-mark { width: 48px; height: 44px; }
  .letterhead .address {
    position: absolute; left: 34px; top: 876px;
    font-style: normal; font-size: 9.5px; line-height: 13.8px;
  }
  .letterhead .signatory {
    position: absolute; left: 34px; top: 950px;
    font-size: 9.5px;
  }
  .letterhead .services { right: 30px; top: 942px; font-size: 15.5px; }
  .letterhead .band { height: 33px; font-size: 16px; letter-spacing: 0.01em; }
</style>
</head>
<body>
<main class="canvas">

  <div class="brand brand--hero">
    <span class="brand-name">The Bristaven<br>Group</span>
    <span class="brand-mark"></span>
  </div>

  <div class="brand brand--mono brand--mono-show">
    <span class="brand-name">The Bristaven<br>Group</span>
    <span class="brand-mark"></span>
  </div>

  <section class="sheet card-front">
    <div class="brand">
      <span class="brand-name">The Bristaven<br>Group</span>
      <span class="brand-mark"></span>
    </div>
    <p class="services">COACHING <span class="sep">|</span> CONSULTING <span class="sep">|</span> ADVISORY</p>
    <div class="band"></div>
  </section>

  <section class="sheet card-back">
    <div class="person">
      <p class="person-name">PAUL DENHOLTZ</p>
      <p class="person-title">President</p>
    </div>
    <ul class="contact">
      <li><span class="key">T:</span> 203.555.0148</li>
      <li><span class="key">E:</span> pdenholtz@bristavengroup.example</li>
      <li><span class="key">A:</span> 14 Corvath Road, Westport, CT 06881</li>
      <li class="web">www.bristavengroup.example</li>
    </ul>
    <div class="band">Unlocking the entrepreneurial spirit | nurturing new ventures</div>
  </section>

  <section class="sheet letterhead">
    <div class="brand">
      <span class="brand-name">The Bristaven<br>Group</span>
      <span class="brand-mark"></span>
    </div>
    <address class="address">
      14 Corvath Road,<br>
      Westport,<br>
      CT 06881<br>
      T: 203.555.0148<br>
      www.bristavengroup.example
    </address>
    <p class="signatory">Paul Denholtz, President</p>
    <p class="services">COACHING <span class="sep">|</span> CONSULTING <span class="sep">|</span> ADVISORY</p>
    <div class="band">Unlocking the entrepreneurial spirit | nurturing new ventures</div>
  </section>

</main>
</body>
</html>
```